Photography Price List DL flyer

In need of a double sided DL flyer to list prices for a photography business that is in the real estate industry. Will need to include logo and be themed to match. Price details and contact information are in the pdf attached.

Below are links to the logo and photos that can be used on the flyer.

Logo
https://www.filquarry.net/s/tmewqoral7bnzx/LogoFiles.zip?dl=0

Photos
https://www.filquarry.net/s/p3vhnkelo81rtw/Website_Images.zip?dl=0

Sorry people the photo examples I put the wrong link. I have fixed it in the brief but the proper link is: https://www.filquarry.net/s/p3vhnkelo81rtw/Website_Images.zip?dl=0

Also dimensions of a DL are 210mm x 99mm + 3m bleed. Thanks

Target Market(s)

Real estate agents

Industry/Entity Type

Business

Requirements
Must have
• Price lists and contact information

```html
<!DOCTYPE html>
<html lang="en">
<head>
<meta charset="utf-8">
<title>Brightside Photos – DL Price Flyer</title>
<link href="https://fonts.googleapis.com/css2?family=Fira+Sans+Extra+Condensed:wght@300;400&family=Open+Sans:wght@400;700&display=swap" rel="stylesheet">
<style>
  :root{
    --bg:#8d96aa;
    --plum-dark:#2a0a1d;
    --plum:#4b1736;
    --plum-mid:#6b2446;
    --rose:#c94a63;
    --salmon:#ec6b6e;
    --lime:#c9d96a;
    --white:#ffffff;
    --grey:#a9a2ad;
    --navy:#1c2234;
    --navy-mid:#27324a;
    --teal:#2f6a6c;
  }
  *{margin:0;padding:0;box-sizing:border-box}
  html,body{width:1200px;height:857px;overflow:hidden;background:var(--bg)}
  body{position:relative;font-family:"Open Sans",sans-serif;color:var(--white)}
  .flyer{position:absolute;width:307px;height:644px;overflow:hidden}
  .flyer--front{left:276px;top:96px;background:linear-gradient(170deg,var(--plum-mid) 0%,var(--plum) 40%,var(--plum-dark) 100%)}
  .flyer--back{left:653px;top:123px;background:var(--navy)}
  .abs{position:absolute}
  .condensed{font-family:"Fira Sans Extra Condensed",sans-serif}
  .center{left:0;width:100%;text-align:center;line-height:1}

  /* brand lockup */
  .brand{position:absolute;display:flex;align-items:center;gap:10px}
  .brand__name{font-family:"Open Sans",sans-serif;font-weight:700;font-size:22px;letter-spacing:2px;color:var(--salmon);white-space:nowrap}
  .brand__dot{width:44px;height:44px;border-radius:50%;background:var(--salmon);flex:none}

  /* front */
  .hero-image{left:0;top:110px;width:307px;height:300px;background:radial-gradient(ellipse at 60% 45%,rgba(190,80,110,.55),rgba(75,23,54,0) 70%)}
  .tagline{top:213px;font-size:21px;font-weight:300}
  .tagline .lime{color:var(--lime)}
  .tagline .rose{color:var(--salmon)}
  .call{top:241px;font-size:23px;font-weight:300;color:var(--grey)}
  .phone-front{top:266px;font-size:44px;font-weight:400}
  .photo{position:absolute;background:linear-gradient(180deg,#c7c9d2 0%,#9aa2b3 45%,#3e3b46 100%);border:2px solid #f2d6d8}
  .photo--one{left:12px;top:342px;width:163px;height:103px;transform:rotate(15deg)}
  .photo--two{left:162px;top:427px;width:137px;height:94px;transform:rotate(-15deg)}
  .photo--three{left:31px;top:483px;width:122px;height:81px}
  .front-contact{top:587px;font-size:12px;font-weight:700;line-height:1.35}

  /* back */
  .back-texture{inset:0;background:
      linear-gradient(125deg,rgba(0,0,0,.55) 0%,rgba(0,0,0,0) 30%),
      radial-gradient(ellipse at 30% 65%,rgba(47,106,108,.75),rgba(47,106,108,0) 60%),
      radial-gradient(ellipse at 85% 40%,rgba(60,70,110,.8),rgba(60,70,110,0) 60%),
      linear-gradient(180deg,var(--navy) 0%,var(--navy-mid) 100%)}
  .prices-title{left:43px;top:132px;font-size:22px;font-weight:400}
  .section{position:absolute;left:43px;font-size:14px;font-weight:700;color:var(--salmon);line-height:1}
  .section::before{content:"";position:absolute;left:-30px;top:13px;width:27px;height:1px;background:var(--salmon)}
  .row{position:absolute;left:43px;font-size:14px;line-height:1;white-space:nowrap}
  .row span{position:absolute;top:0}
  .col-b{left:56px}
  .col-price{left:132px}
  .stripes{left:0;top:535px;width:307px;height:28px}
  .call-back{top:537px;font-size:23px;font-weight:300;color:var(--grey)}
  .phone-back{top:564px;font-size:42px}
  .back-contact{top:610px;font-size:11px;white-space:nowrap}
  .back-contact b{font-weight:400}
</style>
</head>
<body>

<section class="flyer flyer--front" aria-label="Flyer front">
  <div class="abs hero-image" role="img" aria-label="Close-up photograph of a camera lens in warm plum light"></div>
  <svg class="abs" style="left:0;top:0" width="307" height="644" viewBox="0 0 307 644" aria-hidden="true">
    <polygon points="0,345 307,445 307,470 0,365" fill="#8a2e52" opacity=".55"/>
    <polygon points="0,390 307,480 307,560 0,470" fill="#5a1a3a" opacity=".6"/>
    <polygon points="0,500 307,590 307,600 0,510" fill="#8a2e52" opacity=".45"/>
    <rect x="0" y="560" width="307" height="10" fill="#6b2446" opacity=".7"/>
    <rect x="0" y="574" width="307" height="4" fill="#8a2e52" opacity=".5"/>
  </svg>
  <div class="brand" style="left:37px;top:53px">
    <span class="brand__name">BRIGHTSIDE</span>
    <span class="brand__dot"></span>
  </div>
  <p class="abs center condensed tagline"><span class="lime">Brighten</span> <span class="rose">your</span> photos</p>
  <p class="abs center condensed call">CALL US NOW</p>
  <p class="abs center condensed phone-front">0400 555 217</p>
  <div class="photo photo--one" role="img" aria-label="Portrait of a smiling agent against a city skyline"></div>
  <div class="photo photo--two" role="img" aria-label="Portrait of an agent in a suit against a city skyline"></div>
  <div class="photo photo--three" role="img" aria-label="Two agents standing together on a rooftop"></div>
  <p class="abs center front-contact">web: brightsidephotos.com.au<br>email:hello@brightsidephotos.com.au</p>
</section>

<section class="flyer flyer--back" aria-label="Flyer back – price list">
  <div class="abs back-texture" role="img" aria-label="Abstract faceted navy and teal background"></div>
  <div class="brand" style="left:40px;top:55px">
    <span class="brand__name">BRIGHTSIDE</span>
    <span class="brand__dot"></span>
  </div>
  <h1 class="abs prices-title" style="font-weight:400">PRICES</h1>

  <h2 class="section" style="top:183px">PHOTOGRAPHY</h2>
  <p class="row" style="top:211px"><span>10</span><span class="col-b">images</span><span class="col-price">$149</span></p>
  <p class="row" style="top:229px"><span>12 - 15</span><span class="col-b">images</span><span class="col-price">$179</span></p>
  <p class="row" style="top:248px"><span>20+</span><span class="col-b">images</span><span class="col-price">$229</span></p>

  <h2 class="section" style="top:294px">TWILIGHT</h2>
  <p class="row" style="top:322px">Add $100 to image package</p>

  <h2 class="section" style="top:374px">FLOORPLANS</h2>
  <p class="row" style="top:374px"><span class="col-price">$49</span></p>

  <h2 class="section" style="top:424px">VIDEO</h2>
  <p class="row" style="top:457px"><span>30 seconds</span><span class="col-price">$150</span></p>
  <p class="row" style="top:475px"><span>60 seconds</span><span class="col-price">$200</span></p>
  <p class="row" style="top:493px"><span>2&nbsp; minutes</span><span class="col-price">$300</span></p>

  <svg class="abs stripes" viewBox="0 0 307 28" aria-hidden="true">
    <g fill="#ec6b6e">
      <rect x="0" y="0" width="307" height="2"/><rect x="0" y="5" width="307" height="2"/>
      <rect x="0" y="10" width="307" height="2" opacity=".8"/><rect x="0" y="15" width="307" height="2" opacity=".6"/>
      <rect x="0" y="20" width="307" height="2" opacity=".4"/><rect x="0" y="25" width="307" height="2" opacity=".25"/>
    </g>
    <rect x="70" y="0" width="167" height="28" fill="#1f2638"/>
  </svg>
  <p class="abs center condensed call-back">CALL US NOW</p>
  <p class="abs center condensed phone-back">0400 555 217</p>
  <p class="abs center condensed back-contact"><b style="font-weight:700">web:</b> brightsidephotos.com.au &nbsp; <b style="font-weight:700">email:</b> hello@brightsidephotos.com.au</p>
</section>

</body>
</html>
```